Digital Transformation Company Trade Show Banners

I am looking for help designing banners for an upcoming trade show. One would be for our company and one would be for our product. I am planning on purchasing retractable banners with a size of 33" x 81". Details are attached.

```html
<!DOCTYPE html>
<html lang="en">
<head>
<meta charset="utf-8">
<title>Vantrel Retractable Banner</title>
<link href="https://fonts.googleapis.com/css2?family=Oswald:wght@500&family=Barlow:wght@400;600&display=swap" rel="stylesheet">
<style>
  :root {
    --stage: #b9b9b9;
    --paper-top: #ffffff;
    --paper-low: #ececec;
    --ink: #1c1c1c;
    --body-ink: #2a2a2a;
    --orange: #f07a24;
    --blue: #1b72c0;
    --photo-dark: #1d2a44;
    --photo-warm: #b7804e;
  }
  * { margin: 0; padding: 0; box-sizing: border-box; }
  html, body { width: 1200px; height: 900px; overflow: hidden; }
  body {
    background: var(--stage);
    position: relative;
    font-family: "Barlow", sans-serif;
  }
  .banner {
    position: absolute;
    left: 429px;
    top: 30px;
    width: 342px;
    height: 840px;
    overflow: hidden;
    background: linear-gradient(to bottom, var(--paper-top) 0%, var(--paper-top) 28%, var(--paper-low) 55%, #e6e6e6 100%);
  }
  .pixel-field {
    position: absolute;
    border-radius: 4px;
  }
  .pixel-field--top {
    left: 0; top: 0; width: 200px; height: 110px;
    background: radial-gradient(ellipse at 35% 40%, rgba(200,160,120,0.28), rgba(150,150,150,0.12) 55%, transparent 75%);
  }
  .pixel-field--bottom {
    right: 0; bottom: 0; width: 200px; height: 100px;
    background: radial-gradient(ellipse at 70% 65%, rgba(120,110,100,0.3), rgba(200,150,100,0.14) 55%, transparent 78%);
  }
  .brand {
    position: absolute;
    top: 72px;
    left: 0;
    width: 100%;
    display: flex;
    justify-content: center;
    align-items: center;
    gap: 10px;
  }
  .brand__square {
    width: 16px; height: 16px;
    background: var(--blue);
  }
  .brand__name {
    font-family: "Oswald", sans-serif;
    font-weight: 500;
    font-size: 40px;
    letter-spacing: 4px;
    color: var(--orange);
    line-height: 1;
  }
  .hero-photo {
    position: absolute;
    left: 0;
    top: 180px;
    width: 342px;
    height: 230px;
    background: linear-gradient(120deg, var(--photo-dark) 0%, #2f4f8a 22%, #4a4f5a 45%, var(--photo-warm) 75%, #d9c2a6 100%);
  }
  .hero-bands {
    position: absolute;
    left: 0;
    top: 136px;
    width: 342px;
    height: 330px;
  }
  .services {
    position: absolute;
    top: 462px;
    left: 0;
    width: 100%;
    text-align: center;
    font-family: "Oswald", sans-serif;
    font-weight: 500;
    font-size: 26px;
    line-height: 34px;
    text-transform: uppercase;
    color: var(--ink);
    letter-spacing: 0.2px;
  }
  .about {
    position: absolute;
    top: 596px;
    left: 31px;
    width: 280px;
    text-align: center;
    font-size: 12px;
    line-height: 15px;
    color: var(--body-ink);
  }
  .about p + p { margin-top: 12px; }
  .about strong { font-weight: 600; }
  .web-link {
    position: absolute;
    top: 738px;
    left: 66px;
    width: 210px;
    height: 42px;
    background: var(--blue);
    color: #fff;
    font-family: "Oswald", sans-serif;
    font-weight: 500;
    font-size: 25px;
    line-height: 42px;
    text-align: center;
    letter-spacing: 0.5px;
  }
</style>
</head>
<body>
  <div class="banner">
    <div class="pixel-field pixel-field--top" role="img" aria-label="Scattered small squares in orange and grey"></div>
    <div class="pixel-field pixel-field--bottom" role="img" aria-label="Scattered small squares in orange and grey"></div>

    <div class="brand">
      <span class="brand__name">VANTREL</span>
      <span class="brand__square"></span>
    </div>

    <div class="hero-photo" role="img" aria-label="Photo of a laptop showing code on screen, close-up of the keyboard on a desk"></div>

    <svg class="hero-bands" viewBox="0 0 342 330" aria-hidden="true">
      <rect x="0" y="44" width="300" height="5" fill="var(--orange)"/>
      <rect x="0" y="274" width="342" height="5" fill="var(--orange)"/>
      <polygon points="310,0 342,0 342,46 296,46" fill="var(--blue)"/>
      <polygon points="292,40 308,40 268,150 252,150" fill="var(--orange)" opacity="0.75"/>
      <polygon points="342,46 342,60 300,170 286,170" fill="var(--blue)" opacity="0.7"/>
      <polygon points="56,190 72,190 46,255 30,255" fill="var(--blue)" opacity="0.6"/>
      <polygon points="22,271 38,271 18,330 0,330" fill="var(--blue)"/>
      <polygon points="56,275 80,275 64,318 40,318" fill="var(--orange)"/>
    </svg>

    <div class="services">
      <div>Digital Transformation</div>
      <div>Cyber Security</div>
      <div>Software Development</div>
    </div>

    <div class="about">
      <p><strong>Vantrel</strong> is a digital transformation consulting firm dedicated to helping our clients securely and effectively reach their technology goals.</p>
      <p>We provide digital transformation consulting services, cybersecurity services, technology solution services and training &amp; workshops.</p>
    </div>

    <div class="web-link">WWW.VANTREL.IO</div>
  </div>
</body>
</html>
```